Business Card Design

Provide project management services to the construction and other industries
Construction services - Civil and Concrete works
Shop Detailing
Structural Modelling
Client side coordination of project teams and consultants
Feasibility Studies for construction projects

Industry/Entity Type

Business

Contact Information for Business Card

Crestline Ops
Darrel Pikett B.Sc (Eng), M.Proj.Mgt.
Director

m: 0412 583 716
e: dpikett@crestlineops.com.au

p: 08 6293 4078
a: 17 Bramblewood Court, Ashvale, WA 6047

```html
<!DOCTYPE html>
<html lang="en">
<head>
<meta charset="utf-8">
<title>Crestline Ops – Business Card</title>
<link rel="stylesheet" href="https://fonts.googleapis.com/css2?family=Lato:wght@400;700;900&display=swap">
<style>
  :root {
    --green: #0b7d16;
    --green-dark: #086312;
    --white: #ffffff;
    --paper: #f4f4f4;
    --ink: #111111;
    --muted: #1c2a1c;
    --stage: #2a2a2a;
  }
  * { box-sizing: border-box; margin: 0; padding: 0; }
  html, body { width: 1200px; height: 873px; overflow: hidden; }
  body {
    background: var(--stage);
    font-family: "Lato", Arial, sans-serif;
    position: relative;
  }
  .card {
    position: absolute;
    width: 520px;
    height: 318px;
    border-radius: 18px;
    overflow: hidden;
    box-shadow: 0 14px 30px rgba(0,0,0,.55);
    background: var(--green);
  }
  .card--front { left: 50px; top: 278px; }
  .card--back  { left: 630px; top: 278px; }

  .wordmark {
    font-weight: 900;
    font-size: 28px;
    letter-spacing: 1.5px;
    text-transform: uppercase;
    color: var(--ink);
    white-space: nowrap;
  }

  /* Front */
  .front__brand {
    position: absolute; left: 0; top: 0; bottom: 0; width: 236px;
    background: linear-gradient(135deg, var(--white), var(--paper));
    display: flex; align-items: center; justify-content: center;
  }
  .front__brand .wordmark { font-size: 25px; }
  .front__rule {
    position: absolute; top: 0; bottom: 0; width: 4px; background: var(--white);
  }
  .front__rule--a { left: 242px; }
  .front__rule--b { left: 252px; }
  .front__details {
    position: absolute; left: 256px; right: 0; top: 0; bottom: 0;
    padding: 40px 18px 0 34px; color: var(--white);
  }
  .person__name { font-size: 19px; font-weight: 700; }
  .person__quals { font-size: 11px; color: #cfe6cf; margin-top: 5px; }
  .person__role { font-size: 11px; font-weight: 700; color: var(--muted); margin-top: 3px; margin-left: 14px; }
  .contact { list-style: none; margin-top: 26px; }
  .contact li {
    display: flex; align-items: center; gap: 10px;
    font-size: 13px; margin-bottom: 7px; white-space: nowrap;
  }
  .contact svg { width: 21px; height: 21px; flex: none; }
  .address {
    position: absolute; right: 18px; bottom: 26px;
    font-size: 12.5px; font-weight: 700; color: var(--muted); white-space: nowrap;
  }

  /* Back */
  .back__top {
    position: absolute; left: 0; right: 0; top: 0; height: 140px;
    background: linear-gradient(135deg, var(--white), var(--paper));
  }
  .back__top .wordmark { position: absolute; left: 40px; bottom: 22px; font-size: 30px; }
  .back__rule { position: absolute; left: 0; right: 0; height: 3px; background: var(--white); }
  .back__rule--a { top: 145px; }
  .back__rule--b { top: 152px; }
  .services {
    list-style: none; position: absolute; left: 150px; top: 172px; color: var(--white);
  }
  .services li {
    display: flex; align-items: center; gap: 9px;
    font-size: 12.5px; margin-bottom: 7px; white-space: nowrap;
  }
  .services svg { width: 17px; height: 17px; flex: none; }
</style>
</head>
<body>

  <section class="card card--front" aria-label="Business card front">
    <div class="front__brand"><span class="wordmark">Crestline Ops</span></div>
    <div class="front__rule front__rule--a"></div>
    <div class="front__rule front__rule--b"></div>
    <div class="front__details">
      <h1 class="person__name">Darrel Pikett</h1>
      <p class="person__quals">B.Sc (Eng), M.Proj.Mgt.</p>
      <p class="person__role">Director</p>
      <ul class="contact">
        <li>
          <svg viewBox="0 0 24 24" aria-hidden="true"><circle cx="12" cy="12" r="12" fill="#fff"/><path d="M8 6.5l2 0 1 3-1.4 1.2a8 8 0 0 0 3.7 3.7L14.5 13l3 1v2a1.5 1.5 0 0 1-1.6 1.5A10 10 0 0 1 6.5 8.1 1.5 1.5 0 0 1 8 6.5z" fill="var(--green)"/></svg>
          0412 583 716
        </li>
        <li>
          <svg viewBox="0 0 24 24" aria-hidden="true"><circle cx="12" cy="12" r="12" fill="#fff"/><rect x="8.5" y="6" width="7" height="4" fill="var(--green)"/><rect x="6" y="10" width="12" height="6" rx="1" fill="var(--green)"/><rect x="8.5" y="14" width="7" height="4" fill="var(--green)" stroke="#fff" stroke-width="1"/></svg>
          08 6293 4078
        </li>
        <li>
          <svg viewBox="0 0 24 24" aria-hidden="true"><circle cx="12" cy="12" r="12" fill="#fff"/><rect x="6" y="8" width="12" height="8.5" rx="1" fill="var(--green)"/><path d="M6.5 8.5l5.5 4.5 5.5-4.5" fill="none" stroke="#fff" stroke-width="1.2"/></svg>
          dpikett@crestlineops.com.au
        </li>
      </ul>
      <p class="address">17 Bramblewood Court, Ashvale, WA 6047</p>
    </div>
  </section>

  <section class="card card--back" aria-label="Business card back">
    <div class="back__top"><span class="wordmark">Crestline Ops</span></div>
    <div class="back__rule back__rule--a"></div>
    <div class="back__rule back__rule--b"></div>
    <ul class="services">
      <li><svg viewBox="0 0 20 20" aria-hidden="true"><circle cx="10" cy="10" r="10" fill="#fff"/><path d="M5.5 10.5l3 3 6-6.5" fill="none" stroke="var(--green)" stroke-width="2.2"/></svg>Shop Detailing</li>
      <li><svg viewBox="0 0 20 20" aria-hidden="true"><circle cx="10" cy="10" r="10" fill="#fff"/><path d="M5.5 10.5l3 3 6-6.5" fill="none" stroke="var(--green)" stroke-width="2.2"/></svg>Structural Modelling</li>
      <li><svg viewBox="0 0 20 20" aria-hidden="true"><circle cx="10" cy="10" r="10" fill="#fff"/><path d="M5.5 10.5l3 3 6-6.5" fill="none" stroke="var(--green)" stroke-width="2.2"/></svg>Civil &amp; Concrete works</li>
      <li><svg viewBox="0 0 20 20" aria-hidden="true"><circle cx="10" cy="10" r="10" fill="#fff"/><path d="M5.5 10.5l3 3 6-6.5" fill="none" stroke="var(--green)" stroke-width="2.2"/></svg>Feasibility Studies for construction projects</li>
      <li><svg viewBox="0 0 20 20" aria-hidden="true"><circle cx="10" cy="10" r="10" fill="#fff"/><path d="M5.5 10.5l3 3 6-6.5" fill="none" stroke="var(--green)" stroke-width="2.2"/></svg>Client Side coordination of project teams &amp; consultants</li>
    </ul>
  </section>

</body>
</html>
```